Business Cards for new orthopaedic surgery practice

My husband and I are starting our own orthopaedic surgery practice. We are looking for a business card that is uniform, but one will have my name/title and the other will have his. You can just create one design with my name on it for now. But when I choose your design as the winning design I will ask that you add another copy with his name/title.

We are looking for classy, simple, elite all in one. We like dark blues/a little gold/yellow. Something that goes with our logo. We want our logo incorporated. Here is all the info you need:
Business name: RV Spine & Vitality Center
Location: 38157 North Harbor Blvd
Coral Springs, FL 33058
Phone: 954-218-4630
Fax: 954-581-2473
Email: info@myrvspine.example

Names: Lorena Vickers, M.D.
Board Certified Hand and Upper Extremity Surgeon

Eban Sorley, M.D.
Board Certified Hip & Knee Replacement/General Orthopaedic Surgeon

Can decide what you want to put on the back. Maybe a slogan:
Rooted in Care. Focused on You

I am just going to upload our logo. The only thing is if we select you as the winning design, the location, and phone numbers may change. We will need your help to update that once fully solidified.

Industry/Entity Type

Medical

Contact Information for Business Card

Colors
0054AA
0677BA
7BADD7
CADEEF
E8F1F8
0094D4
00A9DD
6FCCEA
C7EBF8
E9F6FB

Requirements
Must have
• class, appeal,
Should not have
• We want to air on the side of masculine if we are looking at masculine vs. feminine feel. But we still want it classy, sophisticated, and something we will love

```html
<!DOCTYPE html>
<html lang="en">
<head>
<meta charset="utf-8">
<title>RV Spine &amp; Vitality Center – Business Cards</title>
<link rel="stylesheet" href="https://fonts.googleapis.com/css2?family=Montserrat:wght@400;500;700&display=swap">
<style>
  :root {
    --stage: #202020;
    --navy: #1b2a57;
    --navy-deep: #15224a;
    --navy-soft: #24366b;
    --gold: #c9a45c;
    --white: #ffffff;
    --ink: #1b1b1b;
  }
  * { box-sizing: border-box; margin: 0; padding: 0; }
  html, body { width: 1200px; height: 711px; overflow: hidden; background: var(--stage); }
  body { position: relative; font-family: "Montserrat", Arial, sans-serif; }

  .card {
    position: absolute;
    width: 540px;
    height: 309px;
    border-radius: 22px;
    border: 3px solid var(--gold);
    overflow: hidden;
    box-shadow: 0 18px 30px rgba(0,0,0,.55);
  }

  /* Back of card */
  .card-back { left: 40px; top: 90px; background: var(--navy); }
  .back-pattern {
    position: absolute; inset: 0;
    background: radial-gradient(circle at 40% 45%, var(--navy-soft) 0%, var(--navy) 55%, var(--navy-deep) 100%);
  }
  .back-mark {
    position: absolute; left: 50%; top: 50%;
    transform: translate(-50%, -50%);
    width: 230px; height: 230px;
    border: 2px solid var(--gold);
    border-radius: 50%;
    display: flex; align-items: center; justify-content: center;
    text-align: center;
  }
  .brand-name {
    font-weight: 700;
    letter-spacing: .08em;
    text-transform: uppercase;
    line-height: 1.35;
  }
  .back-mark .brand-name { color: var(--white); font-size: 19px; width: 180px; }

  /* Front of card */
  .card-front { left: 620px; top: 312px; background: var(--white); }
  .accent-bar {
    position: absolute; left: 18px; top: 64px;
    width: 11px; height: 66px; background: var(--navy);
  }
  .identity { position: absolute; left: 42px; top: 62px; }
  .identity .person-name { font-size: 24px; font-weight: 700; color: var(--navy); line-height: 1.1; }
  .identity .credential { color: var(--gold); }
  .identity .person-title { margin-top: 5px; font-size: 12px; font-weight: 500; color: var(--ink); line-height: 1.3; }

  .contact { position: absolute; left: 42px; top: 196px; font-size: 12.5px; color: var(--ink); line-height: 1.35; }
  .contact .address { margin-bottom: 10px; }
  .contact-line { display: flex; align-items: center; gap: 8px; }
  .contact-line svg { width: 12px; height: 12px; fill: var(--gold); flex: none; }

  .front-mark {
    position: absolute; right: 34px; top: 42px;
    width: 220px; height: 220px;
    border: 2px solid var(--gold);
    border-radius: 50%;
    display: flex; align-items: center; justify-content: center;
    text-align: center;
  }
  .front-mark .brand-name { color: var(--navy); font-size: 19px; width: 175px; }
</style>
</head>
<body>

  <section class="card card-back" aria-label="Card back">
    <div class="back-pattern" role="img" aria-label="Repeating tone-on-tone practice emblem pattern across the navy card"></div>
    <div class="back-mark">
      <p class="brand-name">RV Spine &amp; Vitality Center</p>
    </div>
  </section>

  <section class="card card-front" aria-label="Card front">
    <div class="accent-bar"></div>
    <div class="identity">
      <h1 class="person-name">Lorena Vickers, <span class="credential">M.D.</span></h1>
      <p class="person-title">Board Certified Hand and<br>Upper Extremity Surgeon</p>
    </div>

    <div class="contact">
      <p class="address">38157 North Harbor Blvd<br>Coral Springs, FL 33058</p>
      <p class="contact-line">
        <svg viewBox="0 0 24 24" aria-hidden="true"><path d="M6.6 10.8a15 15 0 0 0 6.6 6.6l2.2-2.2c.3-.3.7-.4 1-.2 1.1.4 2.3.6 3.6.6.6 0 1 .4 1 1V20c0 .6-.4 1-1 1A17 17 0 0 1 3 4c0-.6.4-1 1-1h3.5c.6 0 1 .4 1 1 0 1.3.2 2.5.6 3.6.1.3 0 .7-.2 1z"/></svg>
        954-218-4630
      </p>
      <p class="contact-line">
        <svg viewBox="0 0 24 24" aria-hidden="true"><path d="M6 2h10v5H6zM4 8h16a2 2 0 0 1 2 2v7h-4v5H6v-5H2v-7a2 2 0 0 1 2-2zm4 9v3h8v-3z"/></svg>
        954-581-2473
      </p>
      <p class="contact-line">
        <svg viewBox="0 0 24 24" aria-hidden="true"><path d="M2 5h20v14H2zm2 2v.4l8 5.2 8-5.2V7z"/></svg>
        info@myrvspine.example
      </p>
    </div>

    <div class="front-mark">
      <p class="brand-name">RV Spine &amp; Vitality Center</p>
    </div>
  </section>

</body>
</html>
```